Frostwell Supply - Liquid Nitrogen Business Flyer

I would like a flyer for a direct mailing campaign. The target audience is strictly professional (doctors) and will be mailed to their place of business.
My company (Frostwell Supply) sells and delivers medical liquid nitrogen along with renting accessories that has to do with liquid nitrogen.

The main company is Frostwell Supply; however, Polarvane Holdings (one of the logos are attached) is its parent company and I would like it included in a small way. Around Polarvane Holdings logo - ESTABLISHED 1963

Components of the flyer:

FIRST FILL FREE

Prices are flat rate (no hidden fees... hazmat, delivery, etc.)

-Guarantee -
Will beat any competitor’s price

------Route based services ------
Set-up once and we do the rest
Peace of mind knowing you will have product

----Equipment Rentals----
Dewars-Stands-Cryoguns-Withdrawal Systems

Include ------
Company Name

(555) 382-7164

email address

Some things can be re-worded or left off, your option.. You can ask me questions anytime if any questions arise. If you come up with a "slogan” and use it on the flyer, feel free

Thank you.

Target Market(s)

Dermatologist and Family Doctors

Industry/Entity Type

Business

Colors
f37122
add136
e34297
0255a3

Requirements
Must have
• Catch the mangers eye and relay a positive message very quickly
• Be bright, colorful and CLASSY
• Have 2 sides
• Catchy and smart and abstract WILL win
Nice to have
• The flyer needs to be editable to plug in my information and any changes that might come. I work on Corel Draw X6 for editing.
• 3.74" x 8.27" LONG

```html
<!DOCTYPE html>
<html lang="en">
<head>
<meta charset="utf-8">
<title>Frostwell Supply – Liquid Nitrogen Service Flyer</title>
<link href="https://fonts.googleapis.com/css2?family=Oswald:wght@400;500;700&family=Open+Sans:wght@400;600;700;800&display=swap" rel="stylesheet">
<style>
  :root{
    --orange:#f37122;
    --lime:#add136;
    --magenta:#e34297;
    --magenta-deep:#c8247c;
    --blue:#0255a3;
    --navy:#1b3d7a;
    --ink:#3a3a3a;
    --white:#ffffff;
    --paper:#eef1f5;
  }
  *{margin:0;padding:0;box-sizing:border-box}
  html,body{width:745px;height:1200px;overflow:hidden;background:var(--paper)}
  .flyer{position:relative;width:745px;height:1200px;background:var(--white);overflow:hidden;font-family:"Open Sans",Arial,sans-serif;color:var(--ink)}
  .hero-photo{position:absolute;left:0;top:0;width:745px;height:330px;
    background:linear-gradient(160deg,#f7f9fb 0%,#e4ecf3 45%,#cdd9e6 75%,#f1f4f7 100%)}
  .brand-mark{position:absolute;right:40px;top:250px;display:flex;align-items:center;gap:10px}
  .brand-mark .dot{width:26px;height:26px;border-radius:50%;background:var(--magenta)}
  .brand-mark .name{font-family:"Oswald",sans-serif;font-weight:700;font-size:32px;color:var(--blue);letter-spacing:.5px}

  .offer-band{position:absolute;left:0;top:310px;width:745px;height:260px}
  .offer-lead{position:absolute;left:0;top:412px;width:745px;text-align:center;font-family:"Oswald",sans-serif;font-weight:500;font-size:26px;line-height:34px;color:var(--lime);letter-spacing:.5px}
  .offer-box{position:absolute;left:145px;top:468px;width:455px;height:76px;border:3px solid var(--white);display:flex;align-items:center;justify-content:center;gap:18px;font-family:"Oswald",sans-serif;color:var(--white);text-transform:uppercase}
  .offer-box .small{font-size:42px;font-weight:400;letter-spacing:1px}
  .offer-box .big{font-size:60px;font-weight:700;line-height:1}

  .headline{position:absolute;left:0;top:588px;width:745px;text-align:center;font-family:"Oswald",sans-serif;text-transform:uppercase}
  .headline .line1{font-size:54px;font-weight:700;color:var(--blue);line-height:1.05}
  .headline .line2{font-size:36px;font-weight:700;color:var(--navy);line-height:1.15}

  .courier-art{position:absolute;left:40px;top:712px;width:280px;height:318px;border-radius:6px;
    background:linear-gradient(180deg,#f68a45 0%,var(--orange) 100%);opacity:.92}

  .services{position:absolute;left:340px;top:712px;width:380px}
  .services h2{font-family:"Oswald",sans-serif;font-weight:700;font-size:36px;color:var(--blue);text-transform:uppercase;line-height:1}
  .services .rule{width:245px;height:4px;background:var(--blue);margin:6px 0 14px}
  .service{display:flex;gap:10px;margin-bottom:14px}
  .service svg{flex:none;margin-top:5px}
  .service h3{font-weight:800;font-size:24px;color:var(--magenta-deep);line-height:1.15}
  .service p{font-size:16px;color:var(--ink);line-height:1.3;font-weight:600}

  .parent-mark{position:absolute;right:40px;top:940px;display:flex;align-items:center;gap:8px}
  .parent-mark .square{width:20px;height:20px;background:var(--blue)}
  .parent-mark .name{font-family:"Oswald",sans-serif;font-weight:700;font-size:20px;line-height:26px;color:var(--blue);text-transform:uppercase}
  .parent-est{position:absolute;right:40px;top:968px;font-family:"Oswald",sans-serif;font-weight:700;font-size:13px;line-height:18px;color:var(--blue);letter-spacing:2px}

  .base-band{position:absolute;left:0;top:1000px;width:745px;height:135px}
  .guarantee{position:absolute;left:395px;top:1025px;width:350px;height:66px;background:var(--orange);padding:6px 0 0 18px;color:var(--white)}
  .guarantee h4{font-family:"Oswald",sans-serif;font-weight:700;font-size:27px;text-transform:uppercase;line-height:1;letter-spacing:1px}
  .guarantee p{font-size:16px;font-weight:600;margin-top:4px}
  .flat-rate{position:absolute;left:0;top:1100px;width:745px;text-align:center;font-size:20px;line-height:28px;font-weight:600;color:var(--lime)}

  .contact{position:absolute;left:0;top:1135px;width:745px;height:65px;display:flex;align-items:center;justify-content:center;gap:70px;font-size:22px;font-weight:600;color:var(--ink)}
  .contact span{display:flex;align-items:center;gap:10px}
</style>
</head>
<body>
<main class="flyer">
  <div class="hero-photo" role="img" aria-label="Photograph of a smiling team of doctors in white coats, one giving a thumbs up"></div>
  <div class="brand-mark"><span class="dot"></span><span class="name">Frostwell Supply</span></div>

  <svg class="offer-band" viewBox="0 0 745 260" aria-hidden="true">
    <polygon points="0,0 372,50 745,0 745,22 372,72 0,22" fill="#0255a3"/>
    <polygon points="0,22 372,72 745,22 745,40 372,90 0,40" fill="#e34297"/>
    <polygon points="0,40 372,90 745,40 745,145 0,145" fill="#ffffff"/>
    <polygon points="0,145 745,145 745,235 372,255 0,235" fill="#e34297"/>
  </svg>
  <p class="offer-lead">Mention this flyer and receive</p>
  <div class="offer-box"><span class="small">First Fill</span><span class="big">Free</span></div>

  <div class="headline">
    <div class="line1">Liquid Nitrogen Service</div>
    <div class="line2">and Accessories</div>
  </div>

  <div class="courier-art" role="img" aria-label="Orange silhouette illustration of a delivery worker pushing a hand truck"></div>

  <section class="services">
    <h2>Our Services:</h2>
    <div class="rule"></div>
    <div class="service">
      <svg width="20" height="20" viewBox="0 0 20 20"><polygon points="2,2 18,10 2,18 6,10" fill="#f37122"/></svg>
      <div><h3>Route based services</h3><p>Set-up once and we do the rest Peace of mind knowing you will have product</p></div>
    </div>
    <div class="service">
      <svg width="20" height="20" viewBox="0 0 20 20"><polygon points="2,2 18,10 2,18 6,10" fill="#f37122"/></svg>
      <div><h3>Equipment Rentals</h3><p>Dewars-Stands-Cryoguns-Withdrawal Systems</p></div>
    </div>
  </section>

  <div class="parent-mark"><span class="square"></span><span class="name">Polarvane Holdings</span></div>
  <div class="parent-est">ESTABLISHED 1963</div>

  <svg class="base-band" viewBox="0 0 745 135" aria-hidden="true">
    <polygon points="0,60 745,0 745,135 0,135" fill="#e34297"/>
    <polygon points="0,70 745,12 745,135 0,135" fill="#0255a3"/>
  </svg>
  <div class="guarantee"><h4>Guarantee</h4><p>Will beat any competitor's price</p></div>
  <p class="flat-rate">Prices are flat rate (No Hidden Fees, Hazmat, Delivery, etc.)</p>

  <footer class="contact">
    <span><svg width="26" height="26" viewBox="0 0 24 24"><circle cx="12" cy="12" r="12" fill="#e34297"/><path d="M8.5 6.5l2 2-1.2 1.5a7 7 0 0 0 4.7 4.7l1.5-1.2 2 2-1.3 1.5c-4.5 0-9.7-5.2-9.7-9.7z" fill="#fff"/></svg>(555) 382-7164</span>
    <span><svg width="26" height="26" viewBox="0 0 24 24"><circle cx="12" cy="12" r="12" fill="#e34297"/><rect x="6" y="8" width="12" height="8" fill="#fff"/><polyline points="6,8 12,13 18,8" fill="none" stroke="#e34297" stroke-width="1.4"/></svg>orders@frostwellsupply.com</span>
  </footer>
</main>
</body>
</html>
```